New Look Driving School Project

Current website:
www. kelmorawheelacademy.com

Websites that we like (use content and courses from here as well):
https://www. tollbenroadclass.com

We are looking for a fresh looking driving school website that is easy for students to find the course they are looking for, the price, and allow them to book a lesson all on our website. We would like for this website to have multiple pages: Home, Teen Courses, Adult Courses, About Us, Contact, FAQ, Blog, Requirements.

Target Market(s)

Students in High School or Parents

Industry/Entity Type

Education

Coding

Coded - Design and coding required

Number of Pages Required

5+ page

Font styles to use
Serif
Sans Serif

Colors

Designer to choose colors to be used in the design.

Requirements
Must have
• Must have a form submission and payment processing option. Must have the ability to pick a course, see available times, and process their payment online. MUST BE MOBILE FRIENDLY DESIGN.
Nice to have
• Nice to have a clean format, with big bold fonts.
Should not have
• Should not have a lot of sliders or animations. Should be very fast loading on mobile. Keep it simple but easy to read and elegant.

```html
<!DOCTYPE html>
<html lang="en">
<head>
<meta charset="utf-8">
<title>Kelmora Wheel Academy</title>
<link href="https://fonts.googleapis.com/css2?family=Montserrat:wght@400;500;600;700&family=Nunito:wght@800;900&display=swap" rel="stylesheet">
<style>
  :root {
    --red: #f2124a;
    --red-dark: #d80c3f;
    --navy: #2d3992;
    --navy-dark: #27318a;
    --ink: #1c1c28;
    --white: #ffffff;
    --field-text: #6d6f7c;
    --icon: #9a9caa;
  }
  * { box-sizing: border-box; margin: 0; padding: 0; }
  html, body { width: 1200px; height: 819px; overflow: hidden; background: var(--white); }
  body { font-family: "Montserrat", Arial, sans-serif; color: var(--ink); position: relative; }

  .site-header { position: absolute; left: 0; top: 0; width: 1200px; height: 105px; background: var(--white); }
  .brand { position: absolute; left: 34px; top: 34px; font-family: "Montserrat", Arial, sans-serif; font-weight: 700; font-size: 27px; color: var(--red); letter-spacing: 0.1px; }
  .contact-item { position: absolute; top: 42px; display: flex; align-items: center; gap: 7px; font-size: 13.5px; font-weight: 500; color: var(--ink); }
  .contact-item svg { width: 14px; height: 16px; fill: var(--red); }
  .contact-address { left: 504px; }
  .contact-phone { left: 767px; }
  .call-button { position: absolute; left: 965px; top: 32px; width: 154px; height: 38px; border-radius: 19px; background: var(--red); box-shadow: 0 3px 0 var(--red-dark); color: var(--white); font-size: 12px; font-weight: 600; display: flex; align-items: center; justify-content: center; letter-spacing: 0.3px; }

  .main-nav { position: absolute; left: 0; top: 105px; width: 1200px; height: 58px; background: var(--navy); }
  .main-nav a { position: absolute; top: 21px; color: var(--white); font-size: 12.5px; font-weight: 600; text-decoration: none; letter-spacing: 0.2px; }

  .hero { position: absolute; left: 0; top: 163px; width: 1200px; height: 637px; }
  .hero-photo { position: absolute; left: 0; top: 0; width: 838px; height: 637px;
    background: linear-gradient(115deg, #7b8f62 0%, #a9b69a 22%, #5d7da8 45%, #3f6fb4 62%, #c9a58e 78%, #2e3548 100%); }
  .hero-title { position: absolute; left: 142px; top: 420px; }
  .hero-title span { display: inline-block; font-family: "Nunito", Arial, sans-serif; font-weight: 900; font-size: 45px; line-height: 54px; color: var(--white); padding: 0 14px; }
  .title-top { background: var(--red); margin-left: 4px; }
  .title-bottom { background: var(--navy); display: block !important; width: fit-content; }

  .course-finder { position: absolute; left: 838px; top: 0; width: 362px; height: 637px; background: var(--red); color: var(--white); }
  .finder-title { position: absolute; left: 48px; top: 50px; font-size: 21.5px; font-weight: 500; letter-spacing: 0.2px; }
  .finder-intro { position: absolute; left: 49px; top: 91px; width: 260px; font-size: 12px; font-weight: 600; line-height: 20px; }
  .field { position: absolute; height: 41px; border-radius: 21px; background: var(--white); display: flex; align-items: center; padding-left: 16px; gap: 10px; font-size: 11.5px; font-weight: 500; color: var(--field-text); }
  .field svg { width: 13px; height: 13px; fill: none; stroke: var(--icon); stroke-width: 1.4; }
  .field-wide { left: 49px; width: 293px; }
  .field-half { width: 135px; }
  .field-half::after { content: ""; position: absolute; right: 12px; top: 18px; border: 4px solid transparent; border-top: 5px solid var(--field-text); }
  .col-left { left: 49px; }
  .col-right { left: 207px; }
  .register-button { position: absolute; left: 49px; top: 461px; width: 293px; height: 40px; border-radius: 20px; background: var(--navy); box-shadow: 0 3px 0 var(--navy-dark); display: flex; align-items: center; justify-content: center; font-size: 11.5px; font-weight: 600; color: var(--white); }
  .consent { position: absolute; left: 52px; top: 518px; display: flex; gap: 10px; width: 300px; }
  .consent .box { flex: none; width: 16px; height: 16px; background: #f3f3f5; border-radius: 2px; margin-top: 4px; }
  .consent p { font-size: 11.5px; font-weight: 600; line-height: 20px; }

  .page-foot { position: absolute; left: 0; top: 800px; width: 1200px; height: 19px; background: var(--white); }
</style>
</head>
<body>
  <header class="site-header">
    <div class="brand">Kelmora Wheel Academy</div>
    <div class="contact-item contact-address">
      <svg viewBox="0 0 14 18"><path d="M7 0C3.2 0 0 3 0 6.8 0 11.6 7 18 7 18s7-6.4 7-11.2C14 3 10.8 0 7 0zm0 9.5A2.7 2.7 0 1 1 7 4.1a2.7 2.7 0 0 1 0 5.4z"/></svg>
      LINDEN STREET, VIRGINIA
    </div>
    <div class="contact-item contact-phone">
      <svg viewBox="0 0 16 16"><path d="M3.6 0.5l2.4 3.4c.3.5.2 1.1-.2 1.5L4.5 6.6c.9 2 2.6 3.8 4.7 4.8l1.3-1.3c.4-.4 1-.5 1.5-.2l3.4 2.3c.5.3.7 1 .4 1.5l-.9 1.4c-.5.7-1.4 1.1-2.3.9C6.8 14.9 1.1 9.3.1 3.5-.1 2.6.3 1.7 1 1.2L2.2.3c.5-.3 1.1-.2 1.4.2z"/></svg>
      555-014-2281
    </div>
    <div class="call-button">CALL ME</div>
  </header>

  <nav class="main-nav">
    <a style="left:33px">HOME</a>
    <a style="left:115px">ABOUT US</a>
    <a style="left:224px">FAQ</a>
    <a style="left:292px">TEEN COURSES</a>
    <a style="left:435px">ADULT COURSES</a>
    <a style="left:587px">BLOG</a>
    <a style="left:663px">CONTACTS</a>
    <a style="left:774px">REQUIREMENTS</a>
  </nav>

  <section class="hero">
    <div class="hero-photo" role="img" aria-label="Photo of a smiling student driver in the driver's seat holding up a new licence and giving a thumbs up, with an instructor taking notes beside her"></div>
    <h1 class="hero-title">
      <span class="title-top">The Most Advanced</span>
      <span class="title-bottom">Driving School in Virginia</span>
    </h1>

    <form class="course-finder">
      <h2 class="finder-title">FIND DRIVING COURSES</h2>
      <p class="finder-intro">Send us your details and we'll find the best schedule for you!</p>

      <div class="field field-wide" style="top:145px">
        <svg viewBox="0 0 14 14"><circle cx="7" cy="4" r="3"/><path d="M1.5 13.5c0-3 2.5-5 5.5-5s5.5 2 5.5 5"/></svg>NAME
      </div>
      <div class="field field-wide" style="top:210px">
        <svg viewBox="0 0 14 14"><rect x="1" y="3" width="12" height="8.5"/><path d="M1 3l6 5 6-5"/></svg>EMAIL
      </div>
      <div class="field field-wide" style="top:274px">
        <svg viewBox="0 0 14 14"><path d="M3 1l2 3-1.3 1.3c.8 1.8 2.2 3.2 4 4L9 8l3 2-1 2c-5 0-10-5-10-10z"/></svg>PHONE
      </div>

      <div class="field field-half col-left" style="top:338px">
        <svg viewBox="0 0 14 14"><path d="M2 8l1.5-4h7L12 8v3H2z"/><path d="M2 8h10"/></svg>CITY
      </div>
      <div class="field field-half col-right" style="top:338px">
        <svg viewBox="0 0 14 14"><rect x="1" y="3" width="12" height="8"/><path d="M1 6h12"/></svg>PAYMENT
      </div>
      <div class="field field-half col-left" style="top:404px">
        <svg viewBox="0 0 14 14"><path d="M3 1h8M3 13h8M4 1c0 4 6 4 6 6s-6 2-6 6M10 1c0 4-6 4-6 6s6 2 6 6"/></svg>AGE
      </div>
      <div class="field field-half col-right" style="top:404px">
        <svg viewBox="0 0 14 14"><rect x="1" y="1" width="12" height="12"/><path d="M4 5h6M4 8h6"/></svg>COURSE
      </div>

      <div class="register-button">REGESTER + PAY LATER</div>

      <label class="consent">
        <span class="box"></span>
        <p>Lorem ipsum dolor sit amet, consectetur adipisicing elit, sed do eiusmod tempor incididunt ut labor.</p>
      </label>
    </form>
  </section>

  <div class="page-foot"></div>
</body>
</html>
```